Yoga Studio - Class Timetable Flyer

We require a double sided, size DL (1/3 A4) flyer with our class timetable included.
We would like the final flyer to have.
Side A : Yoga image, logo, address, website, contact phone number, and in big font $40 Introductory Month.
Side B: Clear easy to read timetable, class descriptions and website.
Thank you.
Yours kindly,
Nadia
87d0c7
86cae7
85acd3

```html
<!DOCTYPE html>
<html lang="en">
<head>
<meta charset="utf-8">
<title>Solstice Studio – Class Timetable Flyer</title>
<link rel="stylesheet" href="https://fonts.googleapis.com/css2?family=Quicksand:wght@400;500;600&family=Oswald:wght@600&display=swap">
<style>
  :root{
    --teal:#87d0c7;
    --sky:#86cae7;
    --blue:#85acd3;
    --deep-blue:#3b8fd0;
    --gold:#e6a82a;
    --gold-dark:#b97d12;
    --cream:#efe6cf;
    --ink:#3d3d3d;
    --class-ink:#3577b8;
    --stage:#5a5a5c;
    --white:#ffffff;
  }
  *{box-sizing:border-box;margin:0;padding:0}
  html,body{width:1200px;height:805px;overflow:hidden}
  body{background:var(--stage);font-family:"Quicksand",sans-serif;position:relative}

  .flyer{position:absolute;top:22px;width:370px;height:760px;overflow:hidden;box-shadow:0 6px 18px rgba(0,0,0,.45)}
  .flyer--front{left:165px;background:linear-gradient(180deg,var(--teal) 0%,#7ec6c8 100%)}
  .flyer--back{left:670px;background:var(--white)}
  .flyer svg.decor{position:absolute;inset:0}

  /* front */
  .brand{position:absolute;left:34px;top:40px;display:flex;align-items:center;gap:8px;color:var(--white)}
  .brand__dot{width:14px;height:14px;border-radius:50%;background:var(--white)}
  .brand__name{font-size:22px;font-weight:500;line-height:1}
  .brand__tag{position:absolute;left:56px;top:70px;color:var(--white);font-size:6px;letter-spacing:1.5px}
  .photo{position:absolute;inset:0}
  .offer__arc{position:absolute;inset:0}
  .offer__price{position:absolute;left:60px;top:634px;font-family:"Oswald",sans-serif;font-weight:600;font-size:70px;line-height:1;color:var(--gold);text-shadow:0 2px 0 var(--gold-dark)}
  .offer__month{position:absolute;left:66px;top:710px;font-size:34px;font-weight:500;color:var(--white);line-height:1}
  .contact{position:absolute;right:14px;top:666px;text-align:right;font-size:7.5px;font-style:normal;line-height:1.35;color:var(--ink)}
  .contact p{margin-bottom:7px;display:flex;justify-content:flex-end;align-items:flex-start;gap:5px}
  .contact svg{flex:none;width:7px;height:7px;margin-top:1px}

  /* back */
  .timetable{position:absolute;left:28px;top:18px;width:336px;border-collapse:separate;border-spacing:0;border:1px solid #444;background:var(--white);font-size:7.5px;color:var(--ink);table-layout:fixed}
  .timetable th,.timetable td{border:1px solid #444;text-align:center;padding:2px}
  .timetable thead th{height:40px;vertical-align:bottom;font-weight:500;background:linear-gradient(180deg,#a7dcd8 0 45%,var(--white) 45%)}
  .timetable thead th.time-head{background:var(--white)}
  .timetable td{height:46px}
  .timetable .time{background:linear-gradient(180deg,var(--sky) 0 55%,var(--white) 55%);vertical-align:bottom;text-align:left;font-size:7.5px;padding:0 0 3px 3px}
  .slot{display:block;width:100%;height:38px;border-radius:4px;background:var(--cream)}
  .slot--class{background:transparent;color:var(--class-ink);display:flex;align-items:center;justify-content:center;line-height:1.2}

  .classes{position:absolute;left:22px;top:344px;width:330px}
  .class{margin-bottom:7px}
  .class__title{display:inline-block;padding:3px 26px 3px 10px;color:var(--white);font-size:12.5px;font-weight:500;background:linear-gradient(90deg,var(--deep-blue),var(--sky));border-radius:14px 2px 18px 2px;margin-bottom:5px}
  .class__text{font-size:8px;line-height:1.45;color:var(--ink);padding-left:10px}
</style>
</head>
<body>

<!-- Side A -->
<section class="flyer flyer--front" aria-label="Flyer front">
  <svg class="decor" viewBox="0 0 370 760" aria-hidden="true">
    <path d="M0,0 H210 C150,20 60,60 0,130 Z" fill="var(--sky)"/>
    <path d="M0,130 C60,60 150,20 210,0 H240 C160,30 70,80 0,170 Z" fill="#aee0ea"/>
    <path d="M0,330 C40,220 200,140 370,95 V120 C210,160 60,240 0,380 Z" fill="var(--gold)"/>
    <path d="M0,560 C60,520 150,520 230,540 C300,560 340,610 370,680 V760 C340,660 300,600 220,580 C140,560 60,570 0,610 Z" fill="var(--blue)"/>
    <path d="M0,560 C60,520 150,520 230,540 C300,560 340,610 370,680 V640 C330,580 290,545 230,525 C150,505 60,510 0,540 Z" fill="var(--gold)"/>
  </svg>
  <svg class="photo" viewBox="0 0 370 760" role="img" aria-label="Photo of a woman in an orange top sitting cross-legged in a yoga pose with hands raised, on rocks by the sea at sunset">
    <defs>
      <linearGradient id="sunset" x1="0" y1="0" x2="0" y2="1">
        <stop offset="0" stop-color="#c9a48f"/>
        <stop offset=".45" stop-color="#d9b49c"/>
        <stop offset=".62" stop-color="#9c8a88"/>
        <stop offset="1" stop-color="#6e5a4e"/>
      </linearGradient>
    </defs>
    <path d="M0,335 C50,220 210,150 370,108 V650 C330,590 290,550 230,532 C150,512 60,515 0,548 Z" fill="url(#sunset)"/>
  </svg>

  <div class="brand"><span class="brand__dot"></span><span class="brand__name">Solstice Studio</span></div>
  <p class="brand__tag">YOGA • FITNESS • AQUA</p>

  <svg class="offer__arc" viewBox="0 0 370 760">
    <path id="arch" d="M30,650 Q150,545 268,640" fill="none"/>
    <text font-family="Quicksand, sans-serif" font-size="24" font-weight="500" fill="var(--white)" letter-spacing="1"><textPath href="#arch">INTRODUCTORY</textPath></text>
  </svg>
  <p class="offer__price">$40</p>
  <p class="offer__month">Month</p>

  <address class="contact">
    <p><span>22 Wattle Grove<br>Harmony<br>Vic 3999</span><svg viewBox="0 0 10 10"><path d="M1,5 L5,1 L9,5 V9 H1 Z" fill="var(--ink)"/></svg></p>
    <p><span>0400 555 018</span><svg viewBox="0 0 10 10"><path d="M2,1 L4,1 L5,3 L4,4 C5,6 6,7 7,7 L8,6 L9,8 V9 C5,9 1,5 1,2 Z" fill="var(--ink)"/></svg></p>
    <p><span>nadiaharlow@mailbox.com</span><svg viewBox="0 0 10 10"><rect x="1" y="2" width="8" height="6" fill="var(--ink)"/></svg></p>
    <p><span>www.solsticestudio.com.au</span><svg viewBox="0 0 10 10"><circle cx="5" cy="5" r="4" fill="var(--ink)"/></svg></p>
  </address>
</section>

<!-- Side B -->
<section class="flyer flyer--back" aria-label="Flyer back">
  <svg class="decor" viewBox="0 0 370 760" aria-hidden="true">
    <path d="M0,0 H120 C70,15 30,40 0,80 Z" fill="var(--sky)"/>
    <path d="M0,80 C30,40 70,15 120,0 H140 C80,25 35,60 0,120 Z" fill="var(--teal)"/>
    <path d="M0,722 C80,700 200,715 370,690 V760 H0 Z" fill="var(--teal)"/>
    <path d="M0,712 C90,690 220,705 370,677 V690 C200,715 80,700 0,727 Z" fill="var(--gold)"/>
    <path d="M0,745 C120,725 250,755 370,728 V760 H0 Z" fill="var(--blue)"/>
  </svg>

  <table class="timetable">
    <colgroup><col style="width:42px"><col span="7"></colgroup>
    <thead>
      <tr><th class="time-head"></th><th>Monday</th><th>Tuesday</th><th>Wednesday</th><th>Thursday</th><th>Friday</th><th>Saturday</th><th>Sunday</th></tr>
    </thead>
    <tbody>
      <tr><th class="time">9:30 am</th><td><span class="slot"></span></td><td><span class="slot slot--class">Hot<br>90 mins</span></td><td><span class="slot"></span></td><td><span class="slot slot--class">Power<br>Vinyasa<br>75 mins</span></td><td><span class="slot"></span></td><td><span class="slot slot--class">Power<br>Vinyasa<br>90 mins</span></td><td><span class="slot"></span></td></tr>
      <tr><th class="time">11:00 am</th><td><span class="slot"></span></td><td><span class="slot"></span></td><td><span class="slot"></span></td><td><span class="slot slot--class">Power<br>Essentials<br>60 mins</span></td><td><span class="slot"></span></td><td><span class="slot"></span></td><td><span class="slot"></span></td></tr>
      <tr><th class="time">1:00 pm</th><td><span class="slot"></span></td><td><span class="slot"></span></td><td><span class="slot slot--class">Hot<br>90 mins</span></td><td><span class="slot"></span></td><td><span class="slot"></span></td><td><span class="slot"></span></td><td><span class="slot"></span></td></tr>
      <tr><th class="time">4:30 pm</th><td><span class="slot"></span></td><td><span class="slot"></span></td><td><span class="slot"></span></td><td><span class="slot"></span></td><td><span class="slot"></span></td><td><span class="slot"></span></td><td><span class="slot slot--class">Power<br>Vinyasa<br>90 mins</span></td></tr>
      <tr><th class="time">6:30 pm</th><td><span class="slot slot--class">Power<br>Vinyasa<br>60 mins</span></td><td><span class="slot"></span></td><td><span class="slot slot--class">Hot<br>60 mins</span></td><td><span class="slot"></span></td><td><span class="slot slot--class">Funky<br>Flow<br>75 mins</span></td><td><span class="slot"></span></td><td><span class="slot slot--class">Yin<br>60 mins</span></td></tr>
      <tr><th class="time">7:45 pm</th><td><span class="slot slot--class">Power<br>Essentials<br>60 mins</span></td><td><span class="slot"></span></td><td><span class="slot slot--class">Power<br>Vinyasa<br>60 mins</span></td><td><span class="slot"></span></td><td><span class="slot"></span></td><td><span class="slot"></span></td><td><span class="slot"></span></td></tr>
    </tbody>
  </table>

  <div class="classes">
    <article class="class"><h2 class="class__title">Funky Flow:</h2><p class="class__text">Finish off the week and head into the weekend with a joyful flowing class to a playlist of funky beats.<br>Charity class by donation, suggested $10. Please place cash only in the charity donation box. Frequent guest teachers.</p></article>
    <article class="class"><h2 class="class__title">Hot:</h2><p class="class__text">Dynamic sequence of Strength and Breathing exercises. Suitable for beginners. Heat 37 degrees.</p></article>
    <article class="class"><h2 class="class__title">Power Essentials:</h2><p class="class__text">Flowing Practice with space and time to Align and understand the poses deeply, building muscular strength and endurance. Ideal for beginners.</p></article>
    <article class="class"><h2 class="class__title">Power Vinyasa:</h2><p class="class__text">Strong, Dynamic, Flowing practice ideal for building physical power, flexibility and mental resilience. Heat = 30 degrees</p></article>
    <article class="class"><h2 class="class__title">Yin:</h2><p class="class__text">Long. Slow. Deep practice with a focus on supporting the body to release our deep internal structures of connective tissue.</p></article>
  </div>
</section>

</body>
</html>
```